Curavel - Ensuring better transparency in where drugs are made.

I am developing a consumer advocacy organization called Curavel that is looking at creating a site specifically around better transparency in where your medications are being manufactured. This is a very important topic for me as I am a pharmacist and understand the negative down stream impacts of poor quality in the pharmacy supply chain. Almost every consumer that is prescribed medications likely has no idea about the intricacies behind how their medications reach the shelf in their pharmacies. And most would be shock to understand how many different components have impact on the quality. I have intimate knowledge of this space as I currently oversee all contracting for the third largest GPO in the country. My team manages $10B in pharmaceutical spend and understanding the supply chains for the largest Pharma manufactures in the world is very complex. Below is a article that my team put together about the problem and our solution. Curavel - Is a consumer advocacy organization created to provide more transparency on where your drugs are manufactured.

Where are your drugs made?
Prescription drugs sold in the U.S. are manufactured in facilities located all over the world. Many medications you rely on are made in Australia, Canada, China, India, France, Germany, Japan, Malta, Singapore, Sweden, the United Kingdom, and the United States. Unfortunately, if you live in the U.S., and other countries as well, it can be quite the task to pinpoint exactly where your medication was made because companies are not required to list that information.In fact, drug companies are only required to list the corporate headquarters on the label, but the actual manufacturing facility and its location are usually elsewhere. Complicating matters even more, many pharmaceutical companies, such as Orvan Tesk, BrennerHollowayCo, Dravo, and Kolvat, often use contract manufacturers. This means the company distributing the medication is not the one that manufactured it. Curavel has researched where some of the most popular drugs in the U.S. are made. In the U.S., many brand-name drugs' packaging includes where the drug is made. We have found that 70% of popular brand-name drugs sold in U.S. pharmacies are imported.We've found that some countries are more transparent than others. In Canada, the label often does not specify where the drug is made, but it almost always does on packaging in Turkey.In terms of your safety, wherever the manufacturing location, it is crucial to your health that you take lawfully and properly-manufactured drugs.Oversight in the U.S.Regardless of where they are made, drugs sold in the United States must comply with BMR's rules, which require that drugs are made in accordance with good manufacturing practices to assure quality, and that products are labeled properly to help you safely use them. Domestic and foreign manufacturing plants that manufacture medications for distribution in the U.S. are usually but not always inspected for compliance with BMR regulations (Source: National Civic Review Bureau).Oversight in Canada and Other Highly-developed CountriesAlthough requirements vary across different countries, the most economically advanced countries usually have similar regulations to the U.S. when it comes to manufacturing. For example, Canadians count on their government to regulate medications approved for sale in Canada through Welfare Board's Remedy Standards Division, Canada's equivalent to the U.S. BMR. It's important to note that the U.S. recognizes 25 countries (including Australia, Canada, New Zealand, United Kingdom) as having comparable regulatory oversight as well as pharmaceutical regulatory systems comparable in sophistication and stringency to that of the U.S. This is a premise widely supported by the BMR and American pharmaceutical industry. Many medications sold in those countries are actually made in the U.S.The bottom line is that it is not always easy to determine where a product is manufactured. Your pharmacist is an excellent source for information regarding the medication that he/she dispenses, but we also encourage people to take control of their health and do their own research! Let Curavel help you better understand where your drugs are actually made and the quality of the manufacturing involved.

Target Market(s)

Anyone taking medications.

Industry/Entity Type

Health Care

Logo Text

Curavel

Coding

Coded - Design and coding required

Number of Pages Required

3 page

Colors

Designer to choose colors to be used in the design.

```html
<!DOCTYPE html>
<html lang="en">
<head>
<meta charset="utf-8">
<title>Curavel Consumer Advocacy Organization</title>
<link href="https://fonts.googleapis.com/css2?family=Lato:wght@400;700;900&family=Open+Sans:wght@400;600;700&display=swap" rel="stylesheet">
<style>
:root{
  --blue:#3a86c8;
  --blue-dark:#2f6fa9;
  --navy:#0d2a45;
  --navy-deep:#071a2e;
  --yellow:#fdc96a;
  --yellow-deep:#f5a623;
  --ice:#cfe0f1;
  --ink:#1e1e1e;
  --muted:#8a8f96;
  --line:#e4e8ed;
  --white:#ffffff;
}
*{box-sizing:border-box;margin:0;padding:0}
html,body{width:1200px;height:3416px;overflow:hidden}
body{font-family:"Open Sans",Arial,sans-serif;color:var(--ink);background:var(--white);position:relative}
h1,h2,h3,h4{font-family:"Lato",Helvetica,sans-serif}
a{color:inherit;text-decoration:none}

/* top bar */
.topbar{height:27px;background:var(--blue);color:var(--white);font-size:11px;display:flex;justify-content:space-between;align-items:center;padding-left:160px}
.topbar .contact{display:flex;gap:26px}
.topbar .contact span{display:flex;align-items:center;gap:6px}
.topbar .links{display:flex;height:100%;margin-right:160px}
.topbar .links a{display:flex;align-items:center;padding:0 16px;height:100%}
.topbar .links .signup{background:var(--yellow-deep)}

/* header */
.site-header{height:83px;display:flex;align-items:center;justify-content:space-between;padding:0 160px;border-bottom:1px solid var(--line)}
.brand{display:flex;align-items:center;gap:10px;font-family:"Lato",sans-serif;font-weight:900;font-size:30px;color:var(--blue)}
.brand .mark{width:22px;height:22px;background:var(--blue);border-radius:50%}
.main-nav{display:flex;gap:26px;font-size:10.5px;font-weight:600;text-transform:uppercase;color:#555;align-items:center}
.main-nav .active{color:var(--blue);border-bottom:2px solid var(--blue);padding-bottom:4px}

/* hero */
.hero{height:452px;position:relative;background:linear-gradient(90deg,var(--navy-deep) 0%,var(--navy) 55%,#13324f 100%);color:var(--white);overflow:hidden}
.hero .visual{position:absolute;left:620px;top:0;width:580px;height:452px;background:radial-gradient(circle at 60% 45%,#3b5f7d 0%,#1a3a57 45%,var(--navy-deep) 100%)}
.hero .copy{position:absolute;left:160px;top:118px;width:330px}
.hero .eyebrow{font-family:"Lato",sans-serif;font-size:16px;margin-bottom:10px}
.hero h1{font-size:26px;font-weight:700;line-height:1.3;margin-bottom:14px}
.hero p{font-size:11px;line-height:1.6;margin-bottom:22px}
.btn-pill{display:inline-block;background:var(--blue);color:var(--white);font-size:10px;font-weight:700;text-transform:uppercase;padding:6px 16px;border-radius:14px}
.hero .arrow{position:absolute;left:38px;top:320px;width:34px;height:34px;border:1.5px solid rgba(255,255,255,.8);border-radius:50%}

/* who we are */
.who{height:224px;padding:60px 160px 0}
.section-title{font-size:26px;font-weight:700;display:flex;align-items:center;gap:10px}
.section-title::after{content:"";width:30px;height:2px;background:var(--yellow-deep)}
.who p{margin-top:16px;font-size:10px;line-height:1.75;color:var(--muted)}

/* what we do */
.what{height:414px;display:flex}
.what .copy{width:600px;background:var(--blue);color:var(--white);padding:60px 60px 0 160px}
.what .section-title{color:var(--white)}
.what .section-title::after{background:var(--white)}
.what p{font-size:10.5px;line-height:1.75;margin-top:14px}
.btn-white{display:inline-block;margin-top:18px;background:var(--white);color:var(--blue);font-size:10px;font-weight:700;text-transform:uppercase;padding:8px 22px;border-radius:16px}
.what .visual{flex:1;background:linear-gradient(120deg,#0c1a2c 0%,#1d3b63 50%,#0a1626 100%)}

/* advocate cards */
.advocate{height:435px;padding:59px 160px 0;display:flex;gap:24px}
.adv-card{width:428px;height:317px;background:#f3f7fb;box-shadow:0 2px 6px rgba(0,0,0,.08)}
.adv-card .visual{height:114px;background:linear-gradient(135deg,#2a2f38,#7a6b58)}
.adv-card.lookup .visual{background:linear-gradient(135deg,#e9e4da,#8d7654)}
.adv-card .body{padding:22px 32px}
.adv-card h3{font-size:15px;font-weight:700;margin-bottom:10px}
.adv-card p{font-size:9.5px;line-height:1.75;color:var(--muted)}
.btn-solid{display:inline-block;margin-top:16px;background:var(--blue);color:var(--white);font-size:9px;font-weight:600;text-transform:uppercase;padding:7px 26px;border-radius:14px}
.btn-outline{display:inline-block;margin-top:16px;border:1px solid #b7bcc3;color:#888;font-size:9px;text-transform:uppercase;padding:6px 34px;border-radius:14px}

/* alerts */
.alerts{height:225px;background:var(--yellow);padding:72px 160px 0}
.alerts h2{font-size:22px;font-weight:700;color:var(--white);display:flex;align-items:center;gap:10px}
.alerts h2::after{content:"";width:26px;height:2px;background:var(--white)}
.alert-form{display:flex;margin-top:16px;height:34px}
.alert-form span{flex:1;background:var(--white);border-right:1px solid var(--line);font-size:9.5px;color:#aaa;padding:10px 10px}
.alert-form .submit{flex:0 0 84px;background:var(--blue);color:var(--white);font-weight:700;text-align:center;border:none}

/* audiences */
.audiences{height:355px;padding:91px 160px 0;display:flex;gap:23px}
.aud-card{width:277px;height:203px;border:1.5px solid #9ec3e6;position:relative;padding:66px 22px 0}
.aud-card .icon{position:absolute;left:26px;top:-16px;width:60px;height:60px;border-radius:50%;background:var(--blue);display:flex;align-items:center;justify-content:center}
.aud-card h3{font-size:15px;font-weight:700;margin-bottom:12px}
.aud-card p{font-size:9.5px;line-height:1.7;color:var(--muted)}
.aud-card .more{display:block;margin-top:12px;font-size:9px;font-weight:700;color:var(--blue)}

/* tweet */
.tweets{height:301px;background:var(--ice);position:relative}
.tweet-card{position:absolute;left:312px;top:46px;width:576px;height:182px;background:var(--white);padding:26px 50px}
.tweet-head{display:flex;justify-content:space-between;font-size:11px;font-weight:600;margin-bottom:14px}
.tweet-head .handle{display:flex;align-items:center;gap:8px}
.tweet-head .dot{width:12px;height:12px;border-radius:50%;background:var(--blue)}
.tweet-head .rt{color:#555;font-weight:400}
.tweet-card p{font-size:11px;line-height:1.7;color:var(--muted)}
.tweets .chev{position:absolute;top:130px;font-size:18px;color:#333}
.tweets .dots{position:absolute;left:572px;top:263px;display:flex;gap:6px}
.tweets .dots i{width:11px;height:11px;border:1.5px solid var(--white);border-radius:50%}

/* news */
.news{height:615px;padding:64px 160px 0}
.news h2{font-size:24px;font-weight:700;text-align:center;display:flex;justify-content:center;align-items:center;gap:12px}
.news h2::before,.news h2::after{content:"";width:30px;height:2px;background:var(--yellow-deep)}
.news-grid{display:flex;margin-top:46px;height:341px;box-shadow:0 2px 8px rgba(0,0,0,.08)}
.news-item{flex:1;padding:26px 30px;border-right:1px solid var(--line)}
.news-item:last-child{border-right:none}
.news-item time{font-size:9.5px;color:var(--muted)}
.news-item h3{font-size:15px;font-weight:700;line-height:1.3;margin:12px 0}
.news-item p{font-size:9.5px;line-height:1.8;color:var(--muted)}
.news-item .read{display:block;margin-top:16px;font-size:10px;font-weight:700;color:var(--blue)}
.news .explore{display:block;width:218px;margin:62px auto 0;background:var(--blue);color:var(--white);font-size:10px;font-weight:700;text-transform:uppercase;text-align:center;padding:9px 0;border-radius:16px}

/* footer */
.site-footer{height:250px;background:var(--blue);color:var(--white);padding:56px 160px 0;display:flex}
.foot-col{width:226px}
.foot-col h4{font-size:13px;font-weight:700;text-transform:uppercase;margin-bottom:18px}
.foot-col.news-col h4{text-transform:none;font-size:14px}
.foot-col li{list-style:none;font-size:9.5px;line-height:2.35}
.foot-col .row{display:flex;align-items:center;gap:8px}
.social{display:flex;gap:8px;margin-top:8px}
.social i{width:24px;height:24px;border-radius:50%;background:var(--white)}
.foot-col p{font-size:10px;line-height:1.7}
.signup-field{display:flex;margin-top:14px;border:1px solid var(--white);height:26px;width:200px;font-size:9px}
.signup-field span{flex:1;padding:6px 8px}
.signup-field b{padding:6px 10px;border-left:1px solid var(--white);font-weight:600}
.bottom-bar{height:35px;background:var(--blue-dark);color:var(--white);font-size:10px;display:flex;align-items:center;padding:0 160px}
</style>
</head>
<body>

<div class="topbar">
  <div class="contact">
    <span><svg width="10" height="10" viewBox="0 0 24 24" fill="#fff"><path d="M6.6 10.8a15 15 0 0 0 6.6 6.6l2.2-2.2c.3-.3.7-.4 1-.2 1.1.4 2.3.6 3.6.6.6 0 1 .4 1 1V20c0 .6-.4 1-1 1A17 17 0 0 1 3 4c0-.6.4-1 1-1h3.5c.6 0 1 .4 1 1 0 1.3.2 2.5.6 3.6.1.3 0 .7-.2 1z"/></svg>Phone: +1 555 014 8820</span>
    <span><svg width="11" height="9" viewBox="0 0 24 18" fill="none" stroke="#fff" stroke-width="2"><rect x="1" y="1" width="22" height="16"/><path d="M1 1l11 9 11-9"/></svg>info@curavel.org</span>
  </div>
  <div class="links">
    <a class="signup" href="#">Sign Up</a>
    <a href="#">Get Curavel News</a>
    <a href="#">Advocacy Guidelines</a>
  </div>
</div>

<header class="site-header">
  <div class="brand"><span class="mark"></span>Curavel</div>
  <nav class="main-nav">
    <a class="active" href="#">Home</a>
    <a href="#">Who We Are</a>
    <a href="#">Our Work</a>
    <a href="#">Our Impact</a>
    <a href="#">Get Involved</a>
    <a href="#">Contact Us</a>
    <svg width="11" height="11" viewBox="0 0 24 24" fill="none" stroke="#555" stroke-width="3"><circle cx="10" cy="10" r="7"/><path d="M15 15l7 7"/></svg>
  </nav>
</header>

<section class="hero">
  <div class="visual" role="img" aria-label="Colourful tablets and capsules falling against a dark background"></div>
  <div class="copy">
    <div class="eyebrow">Welcome to</div>
    <h1>Curavel Consumer Advocacy Organization</h1>
    <p>Know where your medicine is made, who made it, and how its quality is checked.</p>
    <a class="btn-pill" href="#">Learn More</a>
  </div>
  <div class="arrow"><svg width="31" height="31" viewBox="0 0 32 32" fill="none" stroke="#fff" stroke-width="1.5"><path d="M18 11l-5 5 5 5M13 16h9"/></svg></div>
</section>

<section class="who">
  <h2 class="section-title">Who We Are</h2>
  <p>Curavel is a consumer advocacy organization founded by pharmacists who manage large pharmaceutical supply chains every day. Prescription drugs sold in the U.S. are made in facilities all over the world, yet labels usually list only a corporate headquarters. Many companies use contract manufacturers, so the brand on the box is often not the maker of the medicine. We research where popular drugs are actually produced, explain how oversight works in each country, and give patients the plain facts they need to ask better questions. Our goal is simple: every person taking a medication should be able to find out where it was made and how its quality is assured.</p>
</section>

<section class="what">
  <div class="copy">
    <h2 class="section-title">What We Do</h2>
    <p>We trace manufacturing sites for widely used medications, compare labeling rules across countries, and publish clear guides so patients understand the path from factory to pharmacy shelf. We work with pharmacists and researchers to check every finding before it is shared.</p>
    <p>We also push for labels that name the real manufacturing facility, and we help people talk with their pharmacist about where their medicines come from.</p>
    <a class="btn-white" href="#">Read More</a>
  </div>
  <div class="visual" role="img" aria-label="Businessman in a suit touching a glowing screen with the word advocacy"></div>
</section>

<section class="advocate">
  <article class="adv-card">
    <div class="visual" role="img" aria-label="Hands writing notes at a meeting table"></div>
    <div class="body">
      <h3>Become an Advocate</h3>
      <p>Join a growing network of patients, pharmacists and caregivers who speak up for clear drug labels. Our free guides help you start conversations in your own community.</p>
      <a class="btn-solid" href="#">Education Directory</a>
    </div>
  </article>
  <article class="adv-card lookup">
    <div class="visual" role="img" aria-label="Scales of justice and a book on a wooden desk"></div>
    <div class="body">
      <h3>Looking for an advocate?</h3>
      <p>Find a trained advocate near you who can help answer questions about where your medication is made and what its quality record shows.</p>
      <a class="btn-outline" href="#">Find an Advocate</a>
    </div>
  </article>
</section>

<section class="alerts">
  <h2>Get Action Alerts</h2>
  <div class="alert-form">
    <span>First Name*</span>
    <span>Last Name*</span>
    <span>Email address*</span>
    <span>Zip Code*</span>
    <span class="submit">SIGN UP</span>
  </div>
</section>

<section class="audiences">
  <article class="aud-card">
    <div class="icon"><svg width="30" height="30" viewBox="0 0 32 32" fill="none" stroke="#fff" stroke-width="2"><rect x="3" y="12" width="18" height="9" rx="4.5" transform="rotate(-35 12 16)"/><path d="M9 11l5 8"/><circle cx="24" cy="22" r="5"/><path d="M20.5 25.5l7-7"/></svg></div>
    <h3>For Medication Manufacturer</h3>
    <p>Learn more about Curavel policies and activities related to key medication issues.</p>
    <a class="more" href="#">LEARN MORE →</a>
  </article>
  <article class="aud-card">
    <div class="icon"><svg width="28" height="28" viewBox="0 0 32 32" fill="none" stroke="#fff" stroke-width="2"><path d="M16 25l-8-8a4.5 4.5 0 0 1 8-5 4.5 4.5 0 0 1 8 5z"/><path d="M6 27h20"/></svg></div>
    <h3>For Volunteers</h3>
    <p>Find out more about Curavel opportunities and events for volunteers.</p>
    <a class="more" href="#">LEARN MORE →</a>
  </article>
  <article class="aud-card">
    <div class="icon"><svg width="26" height="28" viewBox="0 0 28 32" fill="none" stroke="#fff" stroke-width="2"><rect x="4" y="3" width="20" height="26" rx="2"/><path d="M9 10h10M9 15h10M9 20h6"/></svg></div>
    <h3>For the Media</h3>
    <p>Learn more about our impact in recent Curavel press releases, action alerts, and blog posts.</p>
    <a class="more" href="#">LEARN MORE →</a>
  </article>
</section>

<section class="tweets">
  <span class="chev" style="left:330px">‹</span>
  <div class="tweet-card">
    <div class="tweet-head">
      <span class="handle"><i class="dot"></i>@Curavel_updates, 1 day ago</span>
      <span class="rt">⇄&nbsp;&nbsp;Retweet</span>
    </div>
    <p>Did you know most drug labels list only a corporate headquarters, not the factory? Our new guide shows how to find out where your prescription was actually made and what to ask your pharmacist next time.</p>
  </div>
  <span class="chev" style="left:862px">›</span>
  <div class="dots"><i></i><i></i><i></i></div>
</section>

<section class="news">
  <h2>News &amp; Updates</h2>
  <div class="news-grid">
    <article class="news-item">
      <time>Monday, July 1, 2019</time>
      <h3>Where are your drugs made? A new look at labels</h3>
      <p>Our team reviewed packaging for popular brand-name drugs and found that most list only a head office. Here is what that means for patients and how to learn the real source.</p>
      <a class="read" href="#">Read More</a>
    </article>
    <article class="news-item">
      <time>Monday, July 1, 2019</time>
      <h3>Contract makers and the hidden supply chain</h3>
      <p>Many companies rely on outside facilities to produce their medicines. We explain how this works, why it matters for quality, and what oversight applies at each step.</p>
      <a class="read" href="#">Read More</a>
    </article>
    <article class="news-item">
      <time>Monday, July 1, 2019</time>
      <h3>How oversight compares across countries</h3>
      <p>Rules differ around the world, yet many advanced countries share similar standards. Learn which systems are recognized as comparable and where labeling is most open.</p>
      <a class="read" href="#">Read More</a>
    </article>
  </div>
  <a class="explore" href="#">Explore All News &amp; Updates</a>
</section>

<footer class="site-footer">
  <div class="foot-col">
    <h4>Navigation</h4>
    <ul><li>Home</li><li>Who We Are</li><li>Our Work</li><li>Our Impact</li><li>Get Involved</li></ul>
  </div>
  <div class="foot-col">
    <h4>Usefull Links</h4>
    <ul><li>Sitemap</li><li>Contact Us</li><li>Careers</li><li>Media</li><li>Privacy Policy</li></ul>
  </div>
  <div class="foot-col">
    <h4>Contact</h4>
    <ul>
      <li class="row"><svg width="10" height="10" viewBox="0 0 24 24" fill="#fff"><path d="M6.6 10.8a15 15 0 0 0 6.6 6.6l2.2-2.2c.3-.3.7-.4 1-.2 1.1.4 2.3.6 3.6.6.6 0 1 .4 1 1V20c0 .6-.4 1-1 1A17 17 0 0 1 3 4c0-.6.4-1 1-1h3.5c.6 0 1 .4 1 1 0 1.3.2 2.5.6 3.6.1.3 0 .7-.2 1z"/></svg>555-014-8820</li>
      <li class="row"><svg width="10" height="10" viewBox="0 0 24 24" fill="#fff"><rect x="2" y="4" width="20" height="16" rx="2"/></svg>555-014-3391</li>
      <li class="row"><svg width="10" height="10" viewBox="0 0 24 24" fill="#fff"><path d="M2 5h20v14H2z"/></svg>@curavel.desk</li>
    </ul>
    <div class="social"><i></i><i></i></div>
  </div>
  <div class="foot-col news-col">
    <h4>Newsletter Signup</h4>
    <p>Get emails and stay on top of the latest advocacy news</p>
    <div class="signup-field"><span>Email Address</span><b>SIGN UP</b></div>
  </div>
</footer>
<div class="bottom-bar">© 2019 Curavel. All Rights Reserved.</div>

</body>
</html>
```